Young furniture salesman needs own business card to stand out from the rest. Think: simple & sleek.

Hi!

I am a 28 year old highly successful furniture salesman in a store with mostly old timers. The company supplies me with ugly, ancient looking business cards that do not have my cell phone printed on which is a must for my customers and leads who need instant access to me via text, call or email. My design should be easy to create as I prefer a lot of real estate and simplicity in my design. In fact, on the reverse side of my card I would only like a white background with the company logo placed strategically somewhere like in a corner or center bottom so I have plenty of writing space for measurements and sku's etc. Even right smack in the middle may work, as long as it looks clean.

Years ago I had a business card created for a business I had (wood flooring), I will upload a copy of that card so you can mimic it in your own way. The card received many compliments because of the sharpness, simplicity and smoothness. It was also a very thick stock and if possible I would like recommendations on where to I can send your design to be printed in a thick paper stock (matte).

Tip to designers: less is more.
Updates

Target Market(s)

My simple card design should impress young furniture shoppers as I am encountering many young professionals. At the same time the less clutter and easy to read lettering should appeal to old folks. I need a card that says "heres my contact info, reach out to me anytime, however you want, for whatever you need"

Industry/Entity Type

Real Estate

Requirements
Must have
• Side one:
Marco Vellin
Furniture Expert

cell: 555.274.8193
txt: 555.274.8193
store: 555.683.4017
email: mvellin@plovent.com

Side two:

White background (real estate needed for writing purposes)

Company Logo (uploaded)

Either side up to designer:

*Available for appointments 7 days a week for your convenience

Only two COLORS: Blue (supplied in logo) and black
Nice to have
• *** I took a screen shot of a super clean design on a business card a like. Take note of the clean white side with contact info and disregard the side with a photo ***
Should not have
• No restrictions, open to clean cut designs.

```html
<!DOCTYPE html>
<html lang="en">
<head>
<meta charset="utf-8">
<title>Marco Vellin – Business Card</title>
<link href="https://fonts.googleapis.com/css2?family=Mulish:wght@400;700;800&display=swap" rel="stylesheet">
<style>
  :root {
    --backdrop: #e4e4e4;
    --brand-blue: #0a64c0;
    --chair-tone: #5b8fd6;
    --chair-shadow: #1f3f9a;
    --paper: #ffffff;
    --ink: #1a1a1a;
    --on-blue: #ffffff;
  }
  * { margin: 0; padding: 0; box-sizing: border-box; }
  html, body {
    width: 1200px;
    height: 1000px;
    overflow: hidden;
    background: var(--backdrop);
    font-family: "Mulish", sans-serif;
  }
  .card-set {
    position: absolute;
    left: 200px;
    top: 168px;
    display: flex;
    gap: 40px;
  }
  .card {
    position: relative;
    width: 380px;
    height: 663px;
    box-shadow: 0 10px 28px rgba(0, 0, 0, 0.22);
  }
  .card--front {
    background: var(--brand-blue);
    color: var(--on-blue);
    text-align: center;
  }
  .owner-name {
    position: absolute;
    top: 54px;
    width: 100%;
    font-size: 29px;
    font-weight: 800;
    letter-spacing: 0.2px;
  }
  .owner-title {
    position: absolute;
    top: 93px;
    width: 100%;
    font-size: 19px;
    font-weight: 400;
  }
  .chair-art {
    position: absolute;
    left: 90px;
    top: 155px;
    width: 210px;
    height: 290px;
    border-radius: 6px;
    background:
      radial-gradient(ellipse 60% 12% at 50% 90%, var(--chair-shadow) 0%, rgba(31,63,154,0) 100%),
      linear-gradient(180deg, rgba(91,143,214,0.35) 0%, rgba(91,143,214,0.55) 100%);
  }
  .contact-list {
    position: absolute;
    top: 494px;
    width: 100%;
    list-style: none;
    font-size: 22px;
    line-height: 29px;
    font-weight: 400;
  }
  .contact-list .contact-email { font-weight: 800; }
  .card--back { background: var(--paper); }
  .availability {
    position: absolute;
    left: 35px;
    top: 553px;
    font-size: 17px;
    line-height: 22px;
    color: var(--ink);
  }
  .company-name {
    position: absolute;
    right: 22px;
    top: 596px;
    font-size: 28px;
    font-weight: 800;
    color: var(--brand-blue);
    letter-spacing: -0.3px;
  }
</style>
</head>
<body>
  <main class="card-set">
    <section class="card card--front" aria-label="Card front">
      <h1 class="owner-name">Marco Vellin</h1>
      <p class="owner-title">Furniture Expert</p>
      <div class="chair-art" role="img" aria-label="Line drawing of a dining chair with soft shadow beneath"></div>
      <ul class="contact-list">
        <li>cell: 555.274.8193</li>
        <li>txt: 555.274.8193</li>
        <li>store: 555.683.4017</li>
        <li class="contact-email">email: mvellin@plovent.com</li>
      </ul>
    </section>
    <section class="card card--back" aria-label="Card back">
      <p class="availability">Available for<br>appointments<br>7 days a week for<br>your convenience</p>
      <p class="company-name">Plovent</p>
    </section>
  </main>
</body>
</html>
```